Business Card for Ferncliff Massage

I need a business card for my massage therapy & cannabis oil practice. I already have a logo,the "massage" got edited out of this file. I will send the original soon. I need these elements to be on the card:
web: FerncliffMassage.example
ph: 417/283-9061
email: Mirela.Dawkant@mailbox.example
Other slogans, statements to consider:
Science Geek, Massage Therapist, Neuromuscular Therapy, Cannabis Spa Treatments, Raindrop Therapy, Essential Oils
Target Market(s)
women between 20 & 65, people with enough $ to afford regular massage, people who recently had a motor vehicle accident, Halvora HMP insured
Industry/Entity Type
Massage Therapy
Contact Information for Business Card
I would like to see my bear logo featured; contact details, greens & blues preferred colors.

```html
<!DOCTYPE html>
<html lang="en">
<head>
<meta charset="utf-8">
<title>Ferncliff Massage – Business Card</title>
<link rel="stylesheet" href="https://fonts.googleapis.com/css2?family=PT+Sans:wght@400;700&family=Source+Sans+3:wght@400;600&display=swap">
<style>
  :root {
    --backdrop: #727272;
    --card-green: #3a7f3e;
    --card-black: #000000;
    --brand-green: #3f8e42;
    --brand-taupe: #a08b80;
    --text-light: #ffffff;
    --text-soft: #e8f1e8;
    --divider: rgba(255, 255, 255, 0.45);
    --faint-shape: rgba(255, 255, 255, 0.12);
  }
  * { margin: 0; padding: 0; box-sizing: border-box; }
  html, body {
    width: 1200px;
    height: 900px;
    overflow: hidden;
    background: var(--backdrop);
    font-family: "Source Sans 3", "Helvetica Neue", Arial, sans-serif;
  }
  .canvas { position: relative; width: 1200px; height: 900px; }

  .card { position: absolute; overflow: hidden; color: var(--text-light); }

  /* Front */
  .card-front {
    left: 116px; top: 275px; width: 477px; height: 294px;
    background: var(--card-green);
    border-radius: 0 52px 0 52px;
  }
  .card-front .backdrop-shape {
    position: absolute; left: -12px; top: 40px;
    width: 230px; height: 230px; border-radius: 50%;
    background: var(--faint-shape);
  }
  .card-front .divider {
    position: absolute; left: 0; right: 0; top: 186px;
    height: 1px; background: var(--divider);
  }
  .person { position: absolute; left: 35px; top: 131px; }
  .person-name { font-size: 18px; font-weight: 600; line-height: 22px; }
  .person-role { font-size: 14px; line-height: 18px; margin-top: 1px; color: var(--text-soft); }

  .brand {
    position: absolute; display: flex; flex-direction: column; align-items: center;
    font-family: "PT Sans", "Trebuchet MS", sans-serif; font-weight: 400;
    text-align: center; white-space: nowrap;
  }
  .brand-mark { border-radius: 50%; flex: none; }
  .brand-name { display: block; }

  .card-front .brand { left: 313px; top: 30px; width: 120px; color: var(--text-light); }
  .card-front .brand-mark { width: 64px; height: 64px; background: var(--text-light); margin-bottom: 14px; }
  .card-front .brand-name { font-size: 23px; line-height: 24px; }

  .contact { position: absolute; left: 207px; top: 201px; list-style: none; font-size: 13.5px; line-height: 19px; }
  .contact li { display: flex; align-items: center; gap: 8px; }
  .contact li.web { margin-top: 5px; }
  .contact svg { width: 11px; height: 11px; fill: var(--text-light); flex: none; }

  /* Back */
  .card-back {
    left: 622px; top: 276px; width: 477px; height: 293px;
    background: var(--card-black);
    border-radius: 56px 0 56px 0;
  }
  .card-back .brand { left: 46px; top: 108px; width: 140px; color: var(--brand-green); }
  .card-back .brand-mark { width: 92px; height: 92px; background: var(--brand-taupe); margin-bottom: 12px; }
  .card-back .brand-name { font-size: 27px; line-height: 28px; }

  .services { position: absolute; left: 256px; top: 32px; list-style: none; }
  .services li {
    display: flex; align-items: center; gap: 9px;
    font-size: 15.5px; font-weight: 600; line-height: 28.6px;
  }
  .services li::before {
    content: "\00BB"; font-size: 16px; font-weight: 400; line-height: 1;
    position: relative; top: -2px;
  }
</style>
</head>
<body>
<main class="canvas">

  <section class="card card-front" aria-label="Business card front">
    <div class="backdrop-shape" aria-hidden="true"></div>
    <div class="divider"></div>
    <div class="person">
      <p class="person-name">Tomas Reyl</p>
      <p class="person-role">President</p>
    </div>
    <div class="brand">
      <span class="brand-mark"></span>
      <span class="brand-name">Ferncliff<br>Massage</span>
    </div>
    <ul class="contact">
      <li class="phone">
        <svg viewBox="0 0 24 24" aria-hidden="true"><path d="M6.6 10.8a15.1 15.1 0 0 0 6.6 6.6l2.2-2.2a1 1 0 0 1 1-.25 11.4 11.4 0 0 0 3.6.57 1 1 0 0 1 1 1V20a1 1 0 0 1-1 1A17 17 0 0 1 3 4a1 1 0 0 1 1-1h3.5a1 1 0 0 1 1 1c0 1.25.2 2.45.57 3.570a1 1 0 0 1-.25 1z"/></svg>
        417/283-9061
      </li>
      <li class="email">
        <svg viewBox="0 0 24 24" aria-hidden="true"><path d="M2 5h20v2l-10 6L2 7z"/><path d="M2 9l10 6 10-6v10H2z"/></svg>
        Mirela.Dawkant@mailbox.example
      </li>
      <li class="web">FerncliffMassage.example</li>
    </ul>
  </section>

  <section class="card card-back" aria-label="Business card back">
    <div class="brand">
      <span class="brand-mark"></span>
      <span class="brand-name">Ferncliff<br>Massage</span>
    </div>
    <ul class="services">
      <li>Science Geek</li>
      <li>Massage Therapist</li>
      <li>Neuromuscular Therapy</li>
      <li>Cannabis Spa Treatments</li>
      <li>Raindrop Therapy</li>
      <li>Essential Oils</li>
    </ul>
  </section>

</main>
</body>
</html>
```